Modern card design needed for building development company

We are looking for a sharp modern new look for our business cards.
We are a New Zealand based company called TKV Ventures NZ LTD that specialises in subdividing large sections, housing and commercial buildings.
We have attached a photo of the current logo and would like to see it improved somehow as it looks a bit dated.
We are open to any colours.

Target Market(s)

Investors, Property buyers

Industry/Entity Type

Investment

Contact Information for Business Card

TKV VENTURES NZ LTD
www.tkvventuresnz.co.nz

Howard Pennick
Phone +64 21 843 192
Email hdpennick@fernmail.co.nz

Font styles to use
Serif
Sans Serif

Colors
0792cd
33a6d7
85cae6
6b449b
886aae
f04a50
ec1f27
f37122
f68d4d

Requirements
Must have
• Please try and make the logo more modern or if you have a similar one we would like to see it.

```html
<!DOCTYPE html>
<html lang="en">
<head>
<meta charset="utf-8">
<title>TKV Ventures NZ LTD – Business Card</title>
<link rel="stylesheet" href="https://fonts.googleapis.com/css2?family=Oswald:wght@600&family=Open+Sans:wght@400&display=swap">
<style>
  :root {
    --page-bg: #e4e7ea;
    --card-top: #f4f5f6;
    --card-bottom: #dcdfe2;
    --ink: #1b1b1f;
    --brand-blue: #1a6fc0;
    --brand-purple: #2e1a6b;
    --brand-purple-deep: #1f0f4c;
    --icon-blue: #2b8ccf;
  }
  * { margin: 0; padding: 0; box-sizing: border-box; }
  html, body {
    width: 1200px; height: 970px; overflow: hidden;
    background: var(--page-bg);
  }
  .card {
    position: absolute; left: 55px; top: 165px;
    width: 1090px; height: 650px;
    background: linear-gradient(160deg, var(--card-top) 0%, #eceef0 55%, var(--card-bottom) 100%);
    box-shadow: 0 6px 18px rgba(0,0,0,0.18);
    overflow: hidden;
  }
  .card__swoosh { position: absolute; inset: 0; width: 100%; height: 100%; }
  .brand {
    position: absolute; right: 36px; top: 46px;
    display: flex; flex-direction: column; align-items: center; gap: 18px;
  }
  .brand__mark { width: 200px; height: 200px; background: var(--brand-purple); }
  .brand__name {
    font-family: "Oswald", "Arial Narrow", sans-serif;
    font-weight: 600; font-size: 44px; letter-spacing: 0;
    color: var(--ink); line-height: 1; white-space: nowrap;
  }
  .contact {
    position: absolute; left: 70px; top: 376px;
    font-family: "Open Sans", Arial, sans-serif;
    font-size: 27px; color: var(--ink);
    list-style: none;
  }
  .contact__row { display: flex; align-items: center; height: 48px; }
  .contact__icon { width: 24px; height: 24px; margin-right: 14px; flex: none; }
  .contact__sep { margin: 0 22px; }
</style>
</head>
<body>
  <section class="card" aria-label="TKV Ventures NZ LTD business card">
    <svg class="card__swoosh" viewBox="0 0 1090 650" preserveAspectRatio="none" aria-hidden="true">
      <defs>
        <linearGradient id="purpleFill" x1="0" y1="0" x2="1" y2="1">
          <stop offset="0" stop-color="#2e1a6b"/>
          <stop offset="1" stop-color="#1f0f4c"/>
        </linearGradient>
      </defs>
      <path d="M0 578 C 320 625, 720 575, 1090 385 L1090 405 C 720 600, 320 648, 0 598 Z" fill="#1a6fc0"/>
      <path d="M480 650 C 760 615, 960 520, 1090 425 L1090 650 Z" fill="url(#purpleFill)"/>
    </svg>

    <div class="brand">
      <span class="brand__mark"></span>
      <span class="brand__name">TKV VENTURES NZ LTD</span>
    </div>

    <ul class="contact">
      <li class="contact__row">
        <svg class="contact__icon" viewBox="0 0 24 24" aria-hidden="true"><path fill="#2b8ccf" d="M6.6 10.8a15 15 0 0 0 6.6 6.6l2.2-2.2c.3-.3.7-.4 1-.2 1.1.4 2.3.6 3.6.6.6 0 1 .4 1 1V20c0 .6-.4 1-1 1A17 17 0 0 1 3 4c0-.6.4-1 1-1h3.5c.6 0 1 .4 1 1 0 1.3.2 2.5.6 3.6.1.3 0 .7-.2 1z"/></svg>
        <span>+64 21 843 192</span>
      </li>
      <li class="contact__row">
        <svg class="contact__icon" viewBox="0 0 24 24" aria-hidden="true"><rect x="2" y="6" width="20" height="13" fill="#2b8ccf"/><path d="M2 6l10 7 10-7" fill="none" stroke="#fff" stroke-width="1.6"/></svg>
        <span>hdpennick@fernmail.co.nz</span>
        <span class="contact__sep">|</span>
        <svg class="contact__icon" viewBox="0 0 24 24" aria-hidden="true"><circle cx="12" cy="12" r="10" fill="#2b8ccf"/><path d="M2 12h20M12 2c3 3 3 17 0 20M12 2c-3 3-3 17 0 20" fill="none" stroke="#fff" stroke-width="1.4"/></svg>
        <span>www.tkvventuresnz.co.nz</span>
      </li>
      <li class="contact__row">
        <svg class="contact__icon" viewBox="0 0 24 24" aria-hidden="true"><path fill="#2b8ccf" d="M12 2a7 7 0 0 0-7 7c0 5 7 13 7 13s7-8 7-13a7 7 0 0 0-7-7zm0 9.5A2.5 2.5 0 1 1 12 6.5a2.5 2.5 0 0 1 0 5z"/></svg>
        <span>PO BOX 48215, Takapuna, Auckland, New Zealand</span>
      </li>
    </ul>
  </section>
</body>
</html>
```